Startup online payment business - Sporting / Golf, Fairway Tally payment

Background:
Our business name is "Fairway Tally" we provide online payments for golfing services via our website. We currently have a logo used on our website. No other design style has been developed. Our aim is to remove cash payments for service at golf clubs.

Our Key Values:
Quick and easy
Formal and polite
Fun with professional boundary
Mate-ship relationships
100% online digital

What we want from you:
Marketing design to be used on posters and stickers in a retail setting to direct customers to our online payment Chanel.
Design must incorporate attached logo, URL fairwaytally.com.au and our key values can act as a guide the type of design. We have used color Hex#007672 for logo background. We are open to use other colors.

Target Market(s)

Golf clubs and golf players

Industry/Entity Type

Golf Course

Font styles to use
Sans Serif

Requirements
Must have
• Directions to online payment via URL: fairwaytally.com.au
Nice to have
• We like the idea of the slogan: No Cash - No worries. Have attached home screen that will be available from URL link. Consideration if using mobile phone in image. Push the online payment and steps 1. Visit fairwaytally.com 2. Select club 3. Confirm payment
Should not have
• Cartoons

```html
<!DOCTYPE html>
<html lang="en">
<head>
<meta charset="utf-8">
<title>Fairway Tally – No Cash No Worries Poster</title>
<link rel="stylesheet" href="https://fonts.googleapis.com/css2?family=Roboto+Condensed:wght@400;700&family=Teko:wght@400;500&display=swap">
<style>
  :root {
    --teal: #007672;
    --teal-deep: #0b5f5b;
    --gold: #e6c77c;
    --gold-dark: #c9a24f;
    --paper: #f4f4f4;
    --grey: #b9b9b9;
    --ink-light: #eef1f0;
    --headline: "Roboto Condensed", sans-serif;
    --label: "Teko", sans-serif;
  }
  * { box-sizing: border-box; }
  html, body { margin: 0; padding: 0; overflow: hidden; background: var(--paper); }
  .poster {
    position: relative;
    width: 923px;
    height: 1200px;
    overflow: hidden;
    background: linear-gradient(180deg, #f7f7f7 0%, #ececec 60%, #f4f4f4 100%);
    font-family: var(--headline);
  }
  .backdrop { position: absolute; inset: 0; }

  .slogan {
    position: absolute;
    left: 32px;
    top: 12px;
    margin: 0;
    font: 700 84px/82px var(--headline);
    color: #fff;
    letter-spacing: 0.5px;
  }
  .slogan span { display: block; }
  .slogan-url {
    position: absolute;
    left: 36px;
    top: 340px;
    margin: 0;
    font: 500 37px/1 var(--label);
    color: var(--gold);
    letter-spacing: 0.3px;
  }

  .monitor {
    position: absolute;
    left: 406px;
    top: 29px;
    width: 497px;
    height: 382px;
    border-radius: 10px 10px 40px 40px;
    background: linear-gradient(180deg, #1c1c1c 0%, #2a2a2a 65%, #d9d9d9 68%, #a9a9a9 100%);
  }
  .monitor-brand {
    position: absolute;
    left: 424px;
    top: 44px;
    width: 464px;
    height: 244px;
    background: #fafafa;
    display: flex;
    align-items: center;
    justify-content: center;
    font: 700 58px/1 var(--headline);
    color: var(--teal);
  }

  .phone {
    position: absolute;
    left: 65px;
    top: 435px;
    width: 240px;
    height: 451px;
    border-radius: 34px;
    background: linear-gradient(180deg, #e1e1e1 0%, #cfcfcf 100%);
    padding: 60px 12px 56px;
  }
  .phone-screen {
    width: 100%;
    height: 100%;
    background: linear-gradient(180deg, var(--teal) 0%, var(--teal-deep) 100%);
  }

  .steps-count {
    position: absolute;
    left: 0;
    width: 1154px;
    top: 455px;
    margin: 0;
    text-align: center;
    font: 700 118px/1 var(--headline);
    color: var(--teal-deep);
  }
  .steps-title {
    position: absolute;
    left: 410px;
    top: 565px;
    width: 340px;
    height: 53px;
    display: flex;
    align-items: center;
    justify-content: space-between;
    font: 400 43px/1 var(--headline);
    color: var(--teal);
  }
  .steps-title::before,
  .steps-title::after {
    content: "";
    width: 26px;
    height: 53px;
    background: var(--grey);
  }
  .step-list {
    position: absolute;
    left: 400px;
    top: 655px;
    margin: 0;
    padding: 0;
    list-style: none;
    font: 400 36px/64px var(--headline);
    color: var(--teal);
  }

  .values {
    position: absolute;
    left: 38px;
    top: 918px;
    display: flex;
    gap: 13px;
  }
  .value {
    position: relative;
    width: 159px;
    height: 194px;
    padding-top: 76px;
    background: var(--teal-deep);
    background-clip: content-box;
    text-align: center;
  }
  .value::before {
    content: "";
    position: absolute;
    left: 0; right: 0; top: 20px; bottom: 0;
    background: var(--teal-deep);
  }
  .value-icon {
    position: absolute;
    left: 50%;
    top: 0;
    width: 58px;
    height: 58px;
    margin-left: -29px;
    border-radius: 50%;
    background: var(--gold);
    z-index: 1;
  }
  .value-text {
    position: relative;
    margin: 0;
    font: 400 31px/36px var(--label);
    color: var(--ink-light);
    text-transform: uppercase;
  }

  .contact-bar {
    position: absolute;
    left: 38px;
    top: 1129px;
    width: 845px;
    height: 61px;
  }
  .contact-item {
    position: absolute;
    top: 0;
    height: 61px;
    display: flex;
    align-items: center;
    gap: 8px;
    font: 400 28px/1 var(--label);
    color: #2f4a48;
  }
  .contact-phone { left: 26px; }
  .contact-mail { left: 212px; }
  .contact-web { left: 520px; color: var(--gold); font-size: 28px; }
  .contact-item svg { flex: none; }
</style>
</head>
<body>
<main class="poster">
  <svg class="backdrop" width="923" height="1200" viewBox="0 0 923 1200" aria-hidden="true">
    <defs>
      <linearGradient id="goldSweep" x1="0" y1="1" x2="1" y2="0">
        <stop offset="0" stop-color="#b88f3c"/>
        <stop offset="0.5" stop-color="#f2dc9e"/>
        <stop offset="1" stop-color="#d2ae5e"/>
      </linearGradient>
      <linearGradient id="barGrey" x1="0" y1="0" x2="1" y2="0">
        <stop offset="0" stop-color="#bdbdbd"/>
        <stop offset="1" stop-color="#e6e6e6"/>
      </linearGradient>
    </defs>
    <path class="hero-field" d="M0 0 H923 V14 C760 36 620 200 489 351 C380 462 200 522 0 533 Z" fill="var(--teal)"/>
    <path class="hero-sweep" d="M0 533 C200 522 380 462 489 351 C620 200 760 36 923 14 L923 28 C772 55 640 218 506 364 C392 484 212 552 0 574 Z" fill="url(#goldSweep)"/>

    <g class="connectors" fill="none" stroke="var(--teal)" stroke-width="1.6">
      <polyline points="382,677 320,677 250,528"/>
      <polyline points="382,741 318,741 280,652"/>
      <polyline points="382,805 318,805 276,780"/>
    </g>
    <g class="connector-dots" fill="var(--teal)">
      <circle cx="384" cy="677" r="3.5"/>
      <circle cx="384" cy="741" r="3.5"/>
      <circle cx="384" cy="805" r="3.5"/>
    </g>

    <rect x="38" y="1129" width="845" height="61" fill="url(#barGrey)"/>
    <path d="M463 1190 L520 1129 H883 V1190 Z" fill="var(--teal-deep)"/>
  </svg>

  <h1 class="slogan"><span>NO</span><span>CASH</span><span>NO</span><span>WORRIES</span></h1>
  <p class="slogan-url">WWW.FAIRWAYTALLY.COM.AU</p>

  <div class="monitor" role="img" aria-label="Desktop computer monitor displaying the Fairway Tally website"></div>
  <div class="monitor-brand">Fairway Tally</div>

  <div class="phone" role="img" aria-label="Smartphone showing the Fairway Tally payment form: choose club, players and holes, total and submit">
    <div class="phone-screen"></div>
  </div>

  <p class="steps-count">3</p>
  <div class="steps-title">SIMPLE STEPS</div>
  <ol class="step-list">
    <li>Visit fairwaytally.com.au</li>
    <li>Select club</li>
    <li>Confirm payment</li>
  </ol>

  <section class="values">
    <div class="value"><span class="value-icon" role="img" aria-label="Stopwatch icon"></span><p class="value-text">Quick<br>and<br>easy</p></div>
    <div class="value"><span class="value-icon" role="img" aria-label="Business person icon"></span><p class="value-text">Formal<br>and<br>polite</p></div>
    <div class="value"><span class="value-icon" role="img" aria-label="Handshake icon"></span><p class="value-text">Fun with<br>professional<br>boundary</p></div>
    <div class="value"><span class="value-icon" role="img" aria-label="Helping hand climbing icon"></span><p class="value-text">Mate-ship<br>relationships</p></div>
    <div class="value"><span class="value-icon" role="img" aria-label="Cloud touch icon"></span><p class="value-text">100%<br>online digital</p></div>
  </section>

  <footer class="contact-bar">
    <div class="contact-item contact-phone">
      <svg width="22" height="22" viewBox="0 0 22 22" aria-hidden="true"><circle cx="11" cy="11" r="11" fill="var(--teal-deep)"/><path d="M7 5.5 L9 5 L10 8 L8.6 9.2 C9.3 10.8 10.6 12.2 12.3 13 L13.5 11.6 L16.5 12.6 L16 14.8 C11.5 15.2 6.4 10.4 7 5.5 Z" fill="#fff"/></svg>
      1-000-000-0000
    </div>
    <div class="contact-item contact-mail">
      <svg width="22" height="22" viewBox="0 0 22 22" aria-hidden="true"><circle cx="11" cy="11" r="11" fill="var(--teal-deep)"/><rect x="5.5" y="7" width="11" height="8" fill="none" stroke="#fff" stroke-width="1.4"/><path d="M5.5 7 L11 11.5 L16.5 7" fill="none" stroke="#fff" stroke-width="1.4"/></svg>
      EXAMPLE@MAIL.COM
    </div>
    <div class="contact-item contact-web">
      <svg width="24" height="24" viewBox="0 0 24 24" aria-hidden="true"><circle cx="12" cy="12" r="12" fill="var(--gold)"/><path d="M8 6 L17 12 L12.8 12.8 L15 17 L13.3 17.8 L11.2 13.6 L8 16.5 Z" fill="var(--teal-deep)"/></svg>
      WWW.FAIRWAYTALLY.COM.AU
    </div>
  </footer>
</main>
</body>
</html>
```